A property investment company, looking to provide lovely sustainable homes for familys and individua

For a small investment business i am starting which will buy and refurbish unloved houses and apartments to rent out or resell. the company name is my family surname (HARGREAVE). <br/>i would like the design to be simple with maybe some emphasis on an ethical and sustainable/environmentally friendly approach with a branding of maybe trees blended with some houses and or apartments.<br/>The colours i like for this design would be mainly green on either a white or black background.
Target Market(s)
This business card is to be used for professional people such as estate agents
mortgage brokers, solicitors and trades people.
Industry/Entity Type
Real Estate
Contact Information for Business Card
owner/director-Martin hargreave
e-mail-martin@hvholdings.co.uk
website-hargreavehomeholdings.co.uk
mobile-07700945318
landline-02079460581
Look and feel

```html
<!DOCTYPE html>
<html lang="en">
<head>
<meta charset="utf-8">
<title>Hargreave – Business Card</title>
<link rel="stylesheet" href="https://fonts.googleapis.com/css2?family=Open+Sans:wght@400;600;700;800&display=swap">
<style>
  :root {
    --page: #e9e7e2;
    --card: #ffffff;
    --card-shade: #f1f1ef;
    --green: #8cc63f;
    --green-dark: #5d9a22;
    --green-line: #4f8a2a;
    --ink: #1f1f1f;
    --grey: #5b5b5b;
  }
  html, body {
    margin: 0;
    width: 1200px;
    height: 1022px;
    overflow: hidden;
    background: var(--page);
    font-family: "Open Sans", Arial, sans-serif;
  }
  .card {
    position: absolute;
    left: 100px;
    top: 216px;
    width: 1000px;
    height: 590px;
    background: linear-gradient(135deg, var(--card) 0%, var(--card) 55%, var(--card-shade) 100%);
    box-shadow: 0 8px 24px rgba(0,0,0,.18);
    overflow: hidden;
  }
  .brand {
    position: absolute;
    left: 70px;
    top: 150px;
    display: flex;
    align-items: center;
    gap: 14px;
  }
  .brand-mark {
    width: 26px;
    height: 26px;
    background: var(--green);
  }
  .brand-name {
    font-weight: 800;
    font-size: 46px;
    letter-spacing: 1px;
    color: var(--ink);
    line-height: 1;
  }
  .brand-rule {
    position: absolute;
    left: 70px;
    height: 4px;
  }
  .brand-rule.dark { top: 222px; width: 400px; background: var(--ink); }
  .brand-rule.green { top: 236px; width: 440px; height: 3px; background: var(--green); }
  .person {
    position: absolute;
    left: 70px;
    top: 270px;
  }
  .person-name {
    margin: 0;
    font-size: 36px;
    font-weight: 700;
    color: var(--green);
    line-height: 1.1;
  }
  .person-role {
    margin: 4px 0 0;
    font-size: 22px;
    color: var(--grey);
  }
  .contacts {
    position: absolute;
    left: 70px;
    top: 392px;
    margin: 0;
    padding: 0;
    list-style: none;
  }
  .contacts li {
    display: flex;
    align-items: center;
    gap: 14px;
    font-size: 24px;
    color: var(--ink);
    line-height: 36px;
  }
  .contacts svg { width: 22px; height: 22px; flex: none; }
  .divider {
    position: absolute;
    left: 620px;
    top: 70px;
    width: 2px;
    height: 420px;
    background: var(--green-line);
  }
  .ribbon {
    position: absolute;
    right: 0;
    bottom: 0;
    width: 1000px;
    height: 590px;
  }
</style>
</head>
<body>
  <div class="card">
    <div class="brand">
      <span class="brand-mark"></span>
      <span class="brand-name">HARGREAVE</span>
    </div>
    <div class="brand-rule dark"></div>
    <div class="brand-rule green"></div>

    <div class="person">
      <p class="person-name">Martin hargreave</p>
      <p class="person-role">Owner / Director</p>
    </div>

    <ul class="contacts">
      <li>
        <svg viewBox="0 0 24 24"><circle cx="12" cy="12" r="10" fill="none" stroke="#8cc63f" stroke-width="2"/><path d="M8 7c0 5 4 9 9 9l1-2-3-1-1 1c-2-1-3-2-4-4l1-1-1-3z" fill="#8cc63f"/></svg>
        02 079 460 581
      </li>
      <li>
        <svg viewBox="0 0 24 24"><rect x="6" y="2" width="12" height="20" rx="2" fill="none" stroke="#8cc63f" stroke-width="2"/><circle cx="12" cy="18" r="1.3" fill="#8cc63f"/></svg>
        07 700 945 318
      </li>
      <li>
        <svg viewBox="0 0 24 24"><rect x="2" y="5" width="20" height="14" fill="none" stroke="#8cc63f" stroke-width="2"/><path d="M2 5l10 8 10-8M2 19l7-7M22 19l-7-7" fill="none" stroke="#8cc63f" stroke-width="2"/></svg>
        martin@hvholdings.co.uk
      </li>
      <li>
        <svg viewBox="0 0 24 24"><circle cx="12" cy="12" r="10" fill="#8cc63f"/><path d="M2 12h20M12 2c-4 5-4 15 0 20M12 2c4 5 4 15 0 20" fill="none" stroke="#fff" stroke-width="1.5"/></svg>
        hargreavehomeholdings.co.uk
      </li>
    </ul>

    <div class="divider"></div>

    <svg class="ribbon" viewBox="0 0 1000 590" aria-hidden="true">
      <polygon points="1000,300 1000,590 520,590" fill="#b8dc7d"/>
      <polygon points="1000,330 1000,590 580,590" fill="var(--green)"/>
      <polygon points="1000,370 1000,590 660,590" fill="#7ab534"/>
    </svg>
  </div>
</body>
</html>
```